Business Card Design

We have our logo and everything in place. Looking to have a layout for our new business cards designed. These will be printed with a matte finish, possibly rounded corners, and looking to incorporate some cool spot UV layers into the design.

Ive uploaded the existing card front and back as well as our logo.

Card Size Will Be 3.5" x 2"

```html
<!DOCTYPE html>
<html lang="en">
<head>
<meta charset="utf-8">
<title>Ridgeline Deck and Rail – Business Cards</title>
<link href="https://fonts.googleapis.com/css2?family=EB+Garamond:wght@400&display=swap" rel="stylesheet">
<style>
  :root {
    --backdrop: #2b2b2d;
    --card: #25282c;
    --ink: #ffffff;
    --accent: #2f8fd6;
    --rule: #e8e8e8;
  }
  * { margin: 0; padding: 0; box-sizing: border-box; }
  html, body {
    width: 1200px;
    height: 1189px;
    overflow: hidden;
    background: var(--backdrop);
    font-family: "EB Garamond", "Times New Roman", serif;
    color: var(--ink);
  }
  .sheet {
    position: relative;
    width: 1200px;
    height: 1189px;
  }
  .card {
    position: absolute;
    left: 250px;
    width: 700px;
    height: 400px;
    background: var(--card);
    border-radius: 28px;
    box-shadow: 0 10px 30px rgba(0,0,0,0.45);
    overflow: hidden;
  }
  .card--front { top: 150px; }
  .card--back { top: 640px; }

  .brand {
    position: absolute;
    left: 0;
    right: 0;
    text-align: center;
    display: flex;
    justify-content: center;
    align-items: center;
    gap: 14px;
    font-weight: 400;
    color: var(--ink);
    white-space: nowrap;
  }
  .brand__mark {
    width: 14px;
    height: 14px;
    background: var(--ink);
  }
  .card--front .brand { top: 170px; font-size: 50px; }
  .card--back .brand { top: 70px; font-size: 40px; }

  .person {
    position: absolute;
    left: 0;
    right: 0;
    top: 170px;
    display: flex;
    align-items: center;
  }
  .person__rule {
    flex: 1;
    height: 2px;
    background: var(--rule);
  }
  .person__rule--left { margin-top: 40px; }
  .person__rule--right { margin-bottom: 40px; }
  .person__text {
    padding: 0 18px;
    text-align: center;
  }
  .person__name {
    font-size: 34px;
    letter-spacing: 1px;
    text-transform: uppercase;
    line-height: 1.1;
  }
  .person__title {
    font-size: 24px;
    color: var(--accent);
    line-height: 1.1;
  }

  .contact {
    position: absolute;
    left: 0;
    right: 0;
    top: 272px;
    text-align: center;
    font-size: 25px;
    line-height: 1.2;
  }
</style>
</head>
<body>
  <main class="sheet">
    <section class="card card--front" aria-label="Card front">
      <div class="brand"><span class="brand__mark"></span>Ridgeline Deck and Rail</div>
    </section>

    <section class="card card--back" aria-label="Card back">
      <div class="brand"><span class="brand__mark"></span>Ridgeline Deck and Rail</div>
      <div class="person">
        <span class="person__rule person__rule--left"></span>
        <div class="person__text">
          <div class="person__name">Grant Mercer</div>
          <div class="person__title">President</div>
        </div>
        <span class="person__rule person__rule--right"></span>
      </div>
      <div class="contact">
        <div class="contact__phone">403.555.0187</div>
        <div class="contact__email">info@ridgelinedeckrail.com</div>
      </div>
    </section>
  </main>
</body>
</html>
```